Design some Business Cards for Varnholt Networks, Inc.

Using the existing logo, please design business cards for Varnholt Networks, Inc.

Varnholt Networks, Inc. is a Internet Telephony Service provider, providing hosted services, including, but not limited to, PBX, ACD, Desktop, Email, Applications, etc.

```html
<!DOCTYPE html>
<html lang="en">
<head>
<meta charset="utf-8">
<title>Varnholt Networks, Inc. – Business Cards</title>
<link href="https://fonts.googleapis.com/css2?family=Source+Sans+3:wght@400;600;700&display=swap" rel="stylesheet">
<style>
  :root {
    --orange: #f07c14;
    --orange-light: #f7a21c;
    --blue: #1f8fce;
    --blue-dark: #1a5f9e;
    --white: #ffffff;
    --backdrop: #8c8c8c;
    --ink: #1c4f8a;
  }
  * { box-sizing: border-box; margin: 0; padding: 0; }
  html, body { width: 1200px; height: 800px; overflow: hidden; }
  body {
    background: var(--backdrop);
    font-family: "Source Sans 3", sans-serif;
    display: flex;
    align-items: center;
    justify-content: center;
    gap: 40px;
  }
  .card {
    width: 540px;
    height: 308px;
    position: relative;
    overflow: hidden;
    border-radius: 4px;
    box-shadow: 0 10px 24px rgba(0,0,0,.3);
  }

  /* Front */
  .card-front {
    background: radial-gradient(circle at 45% 35%, var(--orange-light), var(--orange) 70%);
    display: flex;
    flex-direction: column;
    align-items: center;
    justify-content: center;
    color: var(--white);
  }
  .brand-front {
    display: flex;
    align-items: center;
    gap: 14px;
  }
  .brand-front .brand-dot {
    width: 44px; height: 44px; border-radius: 50%;
    background: var(--white);
  }
  .brand-front .brand-name {
    font-size: 40px;
    font-weight: 600;
    letter-spacing: 1px;
  }
  .front-url {
    margin-top: 12px;
    font-size: 17px;
    font-weight: 600;
  }

  /* Back */
  .card-back { background: var(--white); }
  .art-area {
    position: absolute;
    left: -60px;
    top: 40px;
    width: 360px;
    height: 360px;
  }
  .brand-back {
    position: absolute;
    right: 26px;
    top: 24px;
    display: flex;
    align-items: center;
    gap: 8px;
  }
  .brand-back .brand-dot {
    width: 24px; height: 24px; border-radius: 50%;
    background: var(--orange);
  }
  .brand-back .brand-name {
    font-size: 22px;
    font-weight: 700;
    color: var(--ink);
  }
  .person {
    position: absolute;
    right: 26px;
    top: 74px;
    text-align: right;
  }
  .person-name { font-size: 26px; color: var(--blue); line-height: 1; }
  .person-title { font-size: 17px; font-weight: 700; color: var(--orange); letter-spacing: .5px; }
  .contact {
    position: absolute;
    right: 26px;
    top: 150px;
    text-align: right;
    font-size: 15px;
    line-height: 1.3;
    color: var(--ink);
  }
  .contact .company { font-size: 16px; }
  .contact .address { font-size: 12px; color: var(--orange); margin-bottom: 2px; }
  .contact-line {
    display: flex;
    justify-content: flex-end;
    align-items: center;
    gap: 5px;
  }
  .contact-line svg { width: 11px; height: 11px; fill: var(--orange); }
</style>
</head>
<body>
  <section class="card card-front">
    <div class="brand-front">
      <span class="brand-dot"></span>
      <span class="brand-name">Varnholt Networks</span>
    </div>
    <div class="front-url">www.varnholtnet.com</div>
  </section>

  <section class="card card-back">
    <svg class="art-area" viewBox="0 0 360 360" role="img" aria-label="Illustration of a support agent wearing a headset inside a blue swoosh">
      <defs>
        <linearGradient id="artFill" x1="0" y1="0" x2="1" y2="1">
          <stop offset="0" stop-color="#1f8fce"/>
          <stop offset="1" stop-color="#f07c14"/>
        </linearGradient>
      </defs>
      <circle cx="180" cy="180" r="180" fill="url(#artFill)"/>
    </svg>

    <div class="brand-back">
      <span class="brand-dot"></span>
      <span class="brand-name">Varnholt Networks</span>
    </div>

    <div class="person">
      <div class="person-name">Dana Whitcombe</div>
      <div class="person-title">DIRECTOR</div>
    </div>

    <div class="contact">
      <div class="company">Varnholt Networks, Inc.</div>
      <div class="address">48 Alder Crest Way, Marlow, OR 97120</div>
      <div class="contact-line">012 555 0147
        <svg viewBox="0 0 12 12"><path d="M2 1h3l1 3-2 1c1 2 2 3 4 4l1-2 3 1v3c-6 0-10-4-10-10z"/></svg>
      </div>
      <div class="contact-line">012 555 0147
        <svg viewBox="0 0 12 12"><rect x="3" y="0" width="6" height="12" rx="1"/></svg>
      </div>
      <div class="contact-line">info@varnholtnet.com
        <svg viewBox="0 0 12 12"><path d="M0 2h12v8H0z M0 2l6 5 6-5" /></svg>
      </div>
      <div class="contact-line">www.varnholtnet.com
        <svg viewBox="0 0 12 12"><circle cx="6" cy="6" r="6"/></svg>
      </div>
    </div>
  </section>
</body>
</html>
```